Business Card for Industrial Distributor

We need a business card design for an industrial distributor. We sell machine parts for the manufacturing and oil industry. We would like the cards to look clean and modern but with a touch of industry.

Our colors are blue/white.

Please feel free to visit our website www.krovelmint.com

Target Market(s)

mexican manufacturers in the automobile/aerospace industry

Industry/Entity Type

Industrial

Colors
ffffff
0555a3

```html
<!DOCTYPE html>
<html lang="en">
<head>
<meta charset="utf-8">
<title>Krovelmint Business Card</title>
<link rel="stylesheet" href="https://fonts.googleapis.com/css2?family=Arimo:wght@400;700&display=swap">
<style>
  :root {
    --brand-blue: #0555a3;
    --deep-blue: #263f98;
    --light-blue: #1f7cc4;
    --ink: #1a1a1a;
    --white: #ffffff;
    --backdrop: #e4e5e8;
  }
  * { box-sizing: border-box; margin: 0; padding: 0; }
  html, body {
    width: 1200px; height: 800px; overflow: hidden;
    background: var(--backdrop);
    font-family: "Arimo", Arial, sans-serif;
  }
  .canvas {
    position: relative; width: 1200px; height: 800px;
    display: flex; align-items: center; justify-content: center; gap: 60px;
  }
  .card {
    position: relative; width: 525px; height: 300px; overflow: hidden;
    border-radius: 3px;
    box-shadow: 0 10px 24px rgba(0,0,0,0.14), 0 2px 4px rgba(0,0,0,0.10);
  }
  /* Front */
  .card-front { background: var(--white); }
  .brand {
    position: absolute; display: flex; align-items: center; gap: 12px;
  }
  .brand-dot {
    width: 34px; height: 34px; border-radius: 50%;
  }
  .brand-name { font-weight: 700; letter-spacing: -0.5px; line-height: 1; }
  .card-front .brand { left: 34px; top: 34px; }
  .card-front .brand-dot { background: var(--deep-blue); }
  .card-front .brand-name { color: var(--deep-blue); font-size: 44px; }
  .address {
    position: absolute; left: 36px; top: 112px;
    color: var(--ink); font-size: 14px; line-height: 18px;
  }
  .contact-list {
    position: absolute; left: 36px; top: 158px; list-style: none;
    color: var(--ink); font-size: 14px; line-height: 18px;
  }
  .contact-list li { display: flex; align-items: center; gap: 7px; }
  .contact-icon { width: 13px; height: 13px; flex: none; }
  .corner-block {
    position: absolute; right: 0; bottom: 0; width: 220px; height: 300px;
    background: linear-gradient(160deg, var(--deep-blue), var(--light-blue) 70%, var(--deep-blue));
    border-top-left-radius: 220px 300px;
  }
  /* Back */
  .card-back {
    background: radial-gradient(ellipse at 52% 48%, #2080c8 0%, #1f5cae 45%, var(--deep-blue) 100%);
  }
  .card-back .brand { left: 50%; top: 96px; transform: translateX(-50%); }
  .card-back .brand-dot { background: var(--white); width: 44px; height: 44px; }
  .card-back .brand-name { color: var(--white); font-size: 56px; }
  .back-url {
    position: absolute; left: 0; right: 0; top: 214px; text-align: center;
    color: var(--white); font-size: 15px; letter-spacing: 0.3px;
  }
</style>
</head>
<body>
<main class="canvas">
  <section class="card card-front" aria-label="Card front">
    <div class="brand">
      <span class="brand-dot"></span>
      <span class="brand-name">Krovelmint</span>
    </div>
    <p class="address">4120 Calloway Mill Rd.<br>Harlingen, TX 78550</p>
    <ul class="contact-list">
      <li>
        <svg class="contact-icon" viewBox="0 0 13 13"><rect width="13" height="13" rx="2" fill="var(--brand-blue)"/><path d="M4 3.2c.5 0 .9 1.4.7 1.8l-.5.5c.4.9 1.3 1.9 2.3 2.3l.5-.5c.4-.2 1.8.2 1.8.7v1c0 .4-.4.7-.9.7C5.3 9.6 3.4 7.7 3.3 4.1c0-.5.3-.9.7-.9z" fill="#fff"/></svg>
        (555) 318-2740
      </li>
      <li>
        <svg class="contact-icon" viewBox="0 0 13 13"><rect width="13" height="13" rx="2" fill="var(--brand-blue)"/><rect x="3" y="5" width="7" height="4" fill="#fff"/><rect x="4.3" y="3" width="4.4" height="2" fill="#fff"/></svg>
        (555) 318-2744
      </li>
      <li>
        <svg class="contact-icon" viewBox="0 0 13 13"><rect width="13" height="13" rx="2" fill="var(--brand-blue)"/><rect x="2.8" y="4" width="7.4" height="5" fill="#fff"/><path d="M2.8 4l3.7 2.8L10.2 4" stroke="var(--brand-blue)" stroke-width="0.9" fill="none"/></svg>
        sales@krovelmint.com
      </li>
      <li>
        <svg class="contact-icon" viewBox="0 0 13 13"><rect width="13" height="13" rx="2" fill="var(--brand-blue)"/><rect x="2.8" y="3.2" width="7.4" height="5.2" fill="#fff"/><rect x="4.5" y="9.2" width="4" height="1" fill="#fff"/></svg>
        www.krovelmint.com
      </li>
    </ul>
    <div class="corner-block"></div>
  </section>

  <section class="card card-back" aria-label="Card back">
    <div class="brand">
      <span class="brand-dot"></span>
      <span class="brand-name">Krovelmint</span>
    </div>
    <p class="back-url">www.krovelmint.com</p>
  </section>
</main>
</body>
</html>
```